Sales banner for E-commerce

This banner is intended for an e-commerce site selling motorcycle equipment and accessories.
The banner announces the sales and leads the customer to an offer of helmets, equipment, and accessories for motorcyclists.
The style of the banner must be modern, elegant, and both show that the prices are attractive and make you want to click to discover the offer of sale products behind it.
I insist on the aesthetics and the marketing side of the banner which are two absolutely essential elements.
Banner format 3840 (W) x 1250 (H)
Updates
Faible participation designers
Target Market(s)
Biker clientele in the general sense
Industry/Entity Type
Ecommerce Equipement et accessoires moto
Requirements
Must have
- Represent or inspire the motorcycle universe.
Nice to have
- The banner must be attractive and make you want to click

```html
<!DOCTYPE html>
<html lang="en">
<head>
<meta charset="UTF-8">
<title>Just For Bikers – Sales Banner</title>
<link href="https://fonts.googleapis.com/css2?family=Poppins:wght@600;700;800&family=Russo+One&family=Yellowtail&family=Montserrat:wght@400;500&display=swap" rel="stylesheet">
<style>
  :root{
    --stage:#353535;
    --banner:#000000;
    --orange:#f39200;
    --white:#ffffff;
    --sky:#b9c9e6;
    --asphalt:#8c8a86;
  }
  *{margin:0;padding:0;box-sizing:border-box;}
  html,body{width:1200px;height:1200px;overflow:hidden;background:var(--stage);}
  .banner{
    position:absolute;left:46px;top:420px;width:1107px;height:360px;
    background:var(--banner);overflow:hidden;
    box-shadow:0 4px 10px rgba(0,0,0,.45);
  }
  .deco{position:absolute;left:0;top:0;width:1107px;height:360px;}
  .txt{position:absolute;white-space:nowrap;}
  .offer-line{
    font-family:"Poppins",sans-serif;font-weight:600;color:var(--white);
    font-size:30px;line-height:1;letter-spacing:2px;left:97px;
  }
  .offer-rule{position:absolute;left:97px;width:72px;height:1px;background:var(--orange);}
  .discount{
    font-family:"Poppins",sans-serif;font-weight:800;font-size:52px;line-height:1;
    letter-spacing:5px;left:96px;
  }
  .discount--value{color:var(--orange);top:164px;}
  .discount--label{color:var(--white);top:210px;letter-spacing:8px;}
  .cta{
    position:absolute;left:97px;top:272px;width:109px;height:30px;background:var(--orange);
    font-family:"Poppins",sans-serif;font-weight:700;font-size:11px;letter-spacing:1.2px;
    color:#111;display:flex;align-items:center;justify-content:center;
  }
  .social{
    left:496px;top:20px;width:116px;text-align:center;
    font-family:"Poppins",sans-serif;font-weight:700;font-size:13px;letter-spacing:2px;color:var(--white);
  }
  .kicker{
    left:513px;top:96px;font-family:"Montserrat",sans-serif;font-weight:500;
    font-size:13.5px;letter-spacing:3px;color:var(--white);
  }
  .headline{
    font-family:"Russo One",sans-serif;color:var(--orange);line-height:1;left:414px;
  }
  .headline--just{top:108px;font-size:86px;letter-spacing:-2px;}
  .headline--for{top:182px;font-size:86px;letter-spacing:46px;}
  .headline-script{
    left:486px;top:212px;font-family:"Yellowtail",cursive;font-size:66px;color:var(--white);
    line-height:1;transform:rotate(-6deg);transform-origin:left center;
  }
  .site-url{
    left:479px;top:326px;font-family:"Montserrat",sans-serif;font-size:9.5px;letter-spacing:2.4px;color:var(--white);
  }
</style>
</head>
<body>
<div class="banner">
  <svg class="deco" viewBox="0 0 1107 360" xmlns="http://www.w3.org/2000/svg">
    <defs>
      <linearGradient id="photoTone" x1="0" y1="0" x2="0" y2="1">
        <stop offset="0" stop-color="#b3c5e8"/>
        <stop offset="0.5" stop-color="#c9d2de"/>
        <stop offset="0.62" stop-color="#9a9894"/>
        <stop offset="1" stop-color="#7d7a76"/>
      </linearGradient>
      <pattern id="whiteDots" width="13.5" height="13.4" patternUnits="userSpaceOnUse">
        <circle cx="1.5" cy="1.5" r="1.2" fill="#fff"/>
      </pattern>
      <pattern id="columnDots" width="6" height="6" patternUnits="userSpaceOnUse">
        <circle cx="1" cy="1" r="0.8" fill="#fff"/>
      </pattern>
      <pattern id="orangeDots" width="12.5" height="9.6" patternUnits="userSpaceOnUse">
        <circle cx="1.5" cy="1.5" r="1.4" fill="#f39200"/>
      </pattern>
    </defs>

    <path class="hero-photo" role="img" aria-label="Photo of a motorcyclist in a racing suit and helmet sitting on a white and orange naked sport bike in an empty lot with buildings behind"
      d="M786,0 L1107,0 L1107,270 C1080,292 1000,345 947,344 C910,343 905,300 913,235 C918,195 870,185 835,210 C800,235 760,250 720,238 C670,222 645,180 652,150 C660,90 720,30 786,0 Z"
      fill="url(#photoTone)"/>

    <path class="swoosh" fill="none" stroke="#fff" stroke-width="2"
      d="M740,0 C700,22 660,60 652,110 C645,160 665,205 705,220 C760,240 800,215 840,190 C880,170 905,175 915,215 C925,260 915,320 960,330 C1010,340 1060,300 1107,265"/>

    <rect x="16" y="17" width="58" height="137" fill="url(#whiteDots)"/>
    <rect x="305" y="116" width="14" height="118" fill="url(#columnDots)"/>
    <rect x="1067" y="17" width="14" height="118" fill="url(#columnDots)"/>
    <rect x="1033" y="299" width="60" height="40" fill="url(#orangeDots)"/>

    <g fill="#f39200">
      <circle cx="179" cy="32" r="4.5"/><circle cx="215" cy="32" r="4.5"/>
      <circle cx="252" cy="32" r="4.5"/><circle cx="289" cy="32" r="4.5"/>
    </g>

    <g stroke="#f39200" stroke-width="1.4" fill="none">
      <path d="M30,323 L42,335 M42,323 L30,335"/>
      <path d="M285,146 L297,158 M297,146 L285,158"/>
      <path d="M747,293 L759,305 M759,293 L747,305"/>
    </g>
    <g stroke="#fff" stroke-width="1.4" fill="none">
      <circle cx="78" cy="329" r="5.5"/>
      <circle cx="316" cy="192" r="5.5"/>
      <circle cx="827" cy="299" r="5.5"/>
    </g>
    <circle cx="502" cy="29" r="5" fill="#fff"/>
  </svg>

  <div class="txt offer-line" style="top:58px;">For</div>
  <div class="offer-rule" style="top:91px;"></div>
  <div class="txt offer-line" style="top:94px;">online</div>
  <div class="offer-rule" style="top:128px;"></div>
  <div class="txt offer-line" style="top:129px;">order</div>
  <div class="txt discount discount--value">20%</div>
  <div class="txt discount discount--label">OFF</div>
  <div class="cta">ORDER NOW</div>

  <div class="txt social">RIDEGEAR</div>
  <div class="txt kicker">NEW ARRIVALS</div>
  <div class="txt headline headline--just">JUST</div>
  <div class="txt headline headline--for">FOR</div>
  <div class="txt headline-script">Bikers</div>
  <div class="txt site-url">www.Lorem ipsum.com</div>
</div>
</body>
</html>
```